Pale Lanterns Old Lane Walk Poster Design

We need an A4 sized poster to promote our weekly true crime tours. This poster will be posted onto community noticeboards.
Lots of information and images can be viewed at the following links:-
www.palelanterns.com.au
www.palelanterns.com.au/bookings/
https://www.facebook.com/palelanternsoldlane/
https://www.examplereviews.com.au/Attraction_Review-g000000-d00000000-Reviews-Pale_Lanterns-Newcastle_Greater_Newcastle_New_South_Wales.html
There are also a number of images for possible use at the following link - we are open to intepretation:-
http://palelanterns.com.au/tour-photographs/
The font on our website is "SpecialElite" so we would like to continue using that font type.
Target Market(s)
Adults 25-65.
Font styles to use
Other font styles liked:
- Special Elite
Colors
Designer to choose colors to be used in the design.
Look and feel
Each slider illustrates characteristics of the customer's brand and the style your logo design should communicate.

```html
<!DOCTYPE html>
<html lang="en">
<head>
<meta charset="utf-8">
<title>Pale Lanterns Old Lane Walk</title>
<link rel="stylesheet" href="https://fonts.googleapis.com/css2?family=Special+Elite&display=block">
<style>
  :root{
    --ink:#1b1b1b;
    --paper:#f4f1ea;
    --blood:#d3272b;
    --night:#2b2b2c;
    --footer:#262627;
    --sepia-a:#6f5a3e;
    --sepia-b:#3e3429;
    --type:"Special Elite","Courier Prime","Courier New",monospace;
  }
  *{margin:0;padding:0;box-sizing:border-box}
  html,body{width:848px;height:1200px;overflow:hidden;background:var(--night)}
  .poster{position:relative;width:848px;height:1200px;overflow:hidden;
    font-family:var(--type);font-weight:400;color:var(--paper)}
  h1,h2{font-weight:400}
  .photo{position:absolute}
  .photo-facade{left:0;top:0;width:380px;height:316px;background:linear-gradient(160deg,var(--sepia-a),var(--sepia-b))}
  .photo-station{left:370px;top:0;width:280px;height:190px;background:linear-gradient(180deg,#5d6266,#3b3e40)}
  .photo-workers{left:646px;top:0;width:202px;height:190px;background:linear-gradient(180deg,#8a8780,#5c5a55)}
  .photo-hotel{left:370px;top:186px;width:224px;height:130px;background:linear-gradient(180deg,#6a675f,#45433e)}
  .photo-gaol{left:590px;top:196px;width:258px;height:126px;background:linear-gradient(180deg,#b1aea5,#77746c)}
  .photo-street{left:0;top:312px;width:848px;height:388px;background:linear-gradient(180deg,#4a4b4c,#2d2e2f 70%,#3d3a33)}
  .photo-cathedral{left:0;top:696px;width:360px;height:284px;background:linear-gradient(180deg,#4e4d50,#2c2b2d)}
  .photo-building{left:352px;top:696px;width:496px;height:344px;background:linear-gradient(180deg,#6b6e72,#4b4d50)}
  .photo-dock{left:0;top:976px;width:360px;height:64px;background:linear-gradient(180deg,#555,#3a3a3a)}
  .shade{position:absolute;left:0;top:696px;width:848px;height:284px;background:rgba(38,38,40,.55)}

  .title{position:absolute;left:24px;top:40px;width:810px;font-size:44px;letter-spacing:0;white-space:nowrap;line-height:1;overflow:hidden}
  .title .lead{color:var(--paper)}
  .title .tail{color:var(--ink)}
  .tagline{position:absolute;left:22px;top:116px;font-size:19px;color:#e8e2d6;white-space:nowrap}
  .tag-rule{position:absolute;left:386px;top:112px;width:2px;height:62px;background:var(--paper)}
  .tag-red{position:absolute;left:393px;top:150px;font-size:19px;color:var(--blood);white-space:nowrap}

  .features{position:absolute;left:26px;top:232px;width:800px;list-style:none}
  .features li{position:relative;padding-left:20px;font-size:24px;line-height:31px;margin-bottom:32px;color:var(--paper)}
  .features li::before{content:"";position:absolute;left:0;top:11px;width:7px;height:7px;border-radius:50%;background:var(--blood)}

  .divider{position:absolute;left:282px;top:694px;width:286px;height:1px;background:var(--paper)}
  .claim{position:absolute;left:0;top:718px;width:848px;text-align:center;font-size:34px;white-space:nowrap}
  .claim .hot{color:var(--blood)}
  .headline{position:absolute;left:0;top:792px;width:848px;text-align:center;font-size:39px;white-space:nowrap}
  .meeting{position:absolute;left:20px;top:852px;width:808px;text-align:center;font-size:17px;line-height:26px;color:#cfcac1}
  .duration{position:absolute;left:22px;top:926px;font-size:30px;white-space:nowrap}
  .duration small{font-size:17px}
  .meta-rule{position:absolute;left:431px;top:932px;width:2px;height:62px;background:var(--paper)}
  .location{position:absolute;left:438px;top:962px;font-size:30px;color:var(--blood);white-space:nowrap}
  .location small{font-size:16px}

  .footer{position:absolute;left:0;top:1040px;width:848px;height:160px;background:var(--footer)}
  .footer-rule{position:absolute;left:615px;top:0;width:2px;height:160px;background:#bdbab3}
  .contact{position:absolute;font-size:19px;color:var(--paper);white-space:nowrap}
  .contact svg{display:block;margin-bottom:8px}
  .c-phone{left:26px;top:22px}
  .c-face{left:332px;top:22px}
  .c-insta{left:24px;top:92px}
  .c-tweet{left:332px;top:92px}
  .brand{position:absolute;left:662px;top:10px;width:140px;height:140px;border-radius:50%;background:var(--blood);
    display:flex;align-items:center;justify-content:center;text-align:center;font-size:20px;line-height:24px;color:var(--paper)}
</style>
</head>
<body>
<div class="poster">
  <div class="photo photo-facade" role="img" aria-label="Sepia photograph of an old sandstone post office facade"></div>
  <div class="photo photo-station" role="img" aria-label="Historic photograph of a railway station platform"></div>
  <div class="photo photo-workers" role="img" aria-label="Historic group photograph of railway workers"></div>
  <div class="photo photo-hotel" role="img" aria-label="Historic photograph of a corner hotel building"></div>
  <div class="photo photo-gaol" role="img" aria-label="Historic photograph of a gaol compound"></div>
  <div class="photo photo-street" role="img" aria-label="Rainy night street scene with a lone figure and a large fig tree"></div>
  <div class="photo photo-cathedral" role="img" aria-label="Cathedral lit at night"></div>
  <div class="photo photo-building" role="img" aria-label="Brick courthouse building at dusk"></div>
  <div class="photo photo-dock" role="img" aria-label="Old wharf sheds"></div>
  <div class="shade"></div>

  <h1 class="title"><span class="lead">Pale Lanterns</span> <span class="tail">Old Lane Walk</span></h1>
  <p class="tagline">TAKE A WALK ON THE DARK SIDE</p>
  <span class="tag-rule"></span>
  <p class="tag-red">REVISIT THE SCENES OF THE CRIMES.</p>

  <ul class="features">
    <li>Retrace the steps of Newcastle's most infamous murderers.</li>
    <li>Descend into the murky world of fraudsters, adulterers and lordly impersonators.</li>
    <li>Unearth the keys to the heart of the Ironbark Murderer.</li>
    <li>Relive a time that proves truth is far stranger than fiction.</li>
    <li>Book your ticket for a unique investigation into a dark and crime ridden history.</li>
  </ul>

  <span class="divider"></span>
  <p class="claim">100% <span class="hot">TRUE -</span> 100% <span class="hot">UNBELIEVABLE</span></p>
  <h2 class="headline">STORIES THE CITY TRIED TO FORGET</h2>
  <p class="meeting">Meets at the corner of Harbour Rd &amp; Quarry St, Newcastle; adjacent to the Old Bond Store and the Stonemason's Yard. Bring comfortable shoes</p>
  <p class="duration">Duration: <small>90 Minutes (approx.)</small></p>
  <span class="meta-rule"></span>
  <p class="location">Location: <small>Newcastle East, NSW</small></p>

  <footer class="footer">
    <span class="footer-rule"></span>
    <div class="contact c-phone">
      <svg width="22" height="22" viewBox="0 0 24 24" aria-hidden="true"><path fill="#d3272b" d="M6.6 10.8a15 15 0 0 0 6.6 6.6l2.2-2.2c.3-.3.7-.4 1-.2 1.1.4 2.3.6 3.6.6.6 0 1 .4 1 1V20c0 .6-.4 1-1 1A17 17 0 0 1 3 4c0-.6.4-1 1-1h3.5c.6 0 1 .4 1 1 0 1.3.2 2.5.6 3.6.1.3 0 .7-.2 1z"/></svg>
      0400118227
    </div>
    <div class="contact c-face">
      <svg width="22" height="22" aria-hidden="true"><rect width="22" height="22" fill="#d3272b"/></svg>
      @palelanternsoldlane
    </div>
    <div class="contact c-insta">
      <svg width="22" height="22" aria-hidden="true"><rect width="22" height="22" fill="#d3272b"/></svg>
      @infopalelanterns
    </div>
    <div class="contact c-tweet">
      <svg width="22" height="22" aria-hidden="true"><rect width="22" height="22" fill="#d3272b"/></svg>
      @palelanternsaust
    </div>
    <div class="brand">Pale<br>Lanterns</div>
  </footer>
</div>
</body>
</html>
```